COOL FUN HIP PPE AD NEEDED FOR MAGAZINE

I'm looking for a fun progressive ad for a Hawaii based business magazine. Create a design that will appeal to a business that's in need of PPE to open safely. Use the Logo provided for BreezeGuard.net. These supplies are critical now for businesses to protect their clients and staff. Produce an ad that's professional, sophisticated, progressive, and to the point.

Target Market(s)

The business community who needs personal protective equipment supplies to open up their businesses safely.

Requirements
Must have
• Full page with bleed
Width 8.25 inches x Height 11.125 inches

PRINT AD FORMATS
 Adobe Illustrator® CC 2014 or earlier, Adobe Photoshop® CC 2014, Adobe InDesign® CC 2014 or earlier.

 4-color CMYK Any layouts containing RGB, Spot or Pantone colors must be converted to their CMYK equivalents. Any layouts found to have a differing color scheme must be revised accordingly. We want to ensure that colors are represented properly, therefore, the client will be notified if there are any inconsistencies in color scheme.

 All screen and printer fonts and all CMYK graphics files included. For InDesign® files, please include PDF X-1a (2001) format with files and turn bleeds on when exporting to PDF if submitting ad with bleeds.

 Offset all crop marks by 0.125".

 EPS and TIFF files: 300dpi resolution with CMYK color or grayscale at actual size with all fonts converted to outlines Press-Ready PDF files are acceptable if all fonts are embedded and images are converted to CMYK at 300 dpi. All PDFs built incorrectly will be sent back to the client for revisions. We are also obligated to alert the client if any graphic elements are under 300 dpi to ensure that advertisements are displayed at their best quality.

```html
<!DOCTYPE html>
<html lang="en">
<head>
<meta charset="utf-8">
<title>BreezeGuard.net – Magazine Ad</title>
<link href="https://fonts.googleapis.com/css2?family=Montserrat:wght@400;500;700;800&display=swap" rel="stylesheet">
<style>
  :root {
    --backdrop: #3b3c3d;
    --cream: #efe6d8;
    --leaf: #6f9a5c;
    --blossom: #eea08e;
    --panel: #f6f6f6;
    --green: #0c8a3c;
    --green-soft: rgba(12, 138, 60, 0.85);
    --grey: #6b6b6b;
    --ink: #2b2b2b;
  }
  * { box-sizing: border-box; margin: 0; padding: 0; }
  html, body { width: 1200px; height: 862px; overflow: hidden; }
  body {
    background: var(--backdrop);
    font-family: "Montserrat", sans-serif;
    position: relative;
  }
  .ad-page {
    position: absolute;
    left: 296px; top: 21px;
    width: 608px; height: 820px;
    overflow: hidden;
  }
  .floral-border {
    position: absolute; inset: 0;
    background:
      radial-gradient(circle at 88% 72%, var(--blossom) 0 5%, transparent 14%),
      radial-gradient(circle at 12% 90%, var(--blossom) 0 4%, transparent 12%),
      radial-gradient(circle at 80% 8%, var(--leaf) 0 6%, transparent 20%),
      radial-gradient(circle at 10% 12%, var(--leaf) 0 6%, transparent 20%),
      radial-gradient(circle at 50% 96%, var(--leaf) 0 5%, transparent 18%),
      var(--cream);
  }
  .content-panel {
    position: absolute;
    left: 56px; top: 62px;
    width: 496px; height: 690px;
    background: var(--panel);
    overflow: hidden;
  }
  .brand {
    position: absolute; top: 40px; left: 0; right: 0;
    display: flex; justify-content: center; align-items: center; gap: 10px;
  }
  .brand-dot {
    width: 22px; height: 22px; border-radius: 50%;
    background: var(--green);
  }
  .brand-name {
    font-weight: 800; font-size: 34px; color: var(--green);
    letter-spacing: -0.5px;
  }
  .headline {
    position: absolute; top: 108px; left: 0; right: 0;
    text-align: center; font-weight: 700; line-height: 1.05;
  }
  .headline .lead { color: var(--grey); font-size: 40px; font-weight: 500; }
  .headline .place { color: var(--green); font-size: 44px; font-weight: 800; }
  .features {
    position: absolute; top: 236px; left: 0; right: 0;
    display: flex; justify-content: center; gap: 70px;
  }
  .feature { text-align: center; width: 110px; }
  .feature svg { width: 62px; height: 62px; display: block; margin: 0 auto 8px; }
  .feature p {
    font-size: 11px; font-weight: 500; color: var(--ink);
    text-transform: uppercase; line-height: 1.3;
  }
  .pitch {
    position: absolute; top: 380px; left: 0; right: 0;
    text-align: center; text-transform: uppercase;
    font-size: 25px; font-weight: 500; color: var(--grey); line-height: 1.15;
    z-index: 1;
  }
  .pitch strong { color: var(--green); font-weight: 800; }
  .palm-art {
    position: absolute; bottom: 0;
  }
  .palm-art-left {
    left: 0; width: 82px; height: 380px;
    background: linear-gradient(90deg, var(--green-soft), rgba(12,138,60,0.15));
    border-top-right-radius: 60px;
  }
  .palm-art-right {
    right: 0; width: 112px; height: 176px;
    background: linear-gradient(270deg, var(--green-soft), rgba(12,138,60,0.15));
    border-top-left-radius: 60px;
  }
  .contact {
    position: absolute; left: 150px; bottom: 34px;
    font-size: 13px; font-style: normal; color: var(--ink); line-height: 1.55;
  }
  .contact-icons { display: flex; gap: 4px; margin-bottom: 4px; }
  .contact-icons svg { width: 14px; height: 14px; }
</style>
</head>
<body>
  <main class="ad-page">
    <div class="floral-border" role="img" aria-label="Watercolour border of palm fronds and pink hibiscus flowers on cream"></div>

    <section class="content-panel">
      <div class="brand">
        <span class="brand-dot"></span>
        <span class="brand-name">BreezeGuard.net</span>
      </div>

      <h1 class="headline">
        <span class="lead">WE’VE GOT YOU</span><br>
        <span class="place">HAWAII!</span>
      </h1>

      <div class="features">
        <div class="feature">
          <svg viewBox="0 0 64 64" aria-hidden="true">
            <circle cx="32" cy="32" r="29" fill="none" stroke="var(--green)" stroke-width="3"/>
            <path d="M18 46V26l14-8 14 8v20z" fill="var(--green)"/>
            <rect x="24" y="32" width="16" height="14" fill="var(--panel)"/>
            <rect x="26" y="36" width="5" height="4" fill="var(--green)"/>
            <rect x="32" y="36" width="5" height="4" fill="var(--green)"/>
            <rect x="29" y="41" width="5" height="4" fill="var(--green)"/>
          </svg>
          <p>Locally<br>Stocked</p>
        </div>
        <div class="feature">
          <svg viewBox="0 0 64 64" aria-hidden="true">
            <circle cx="32" cy="32" r="29" fill="none" stroke="var(--green)" stroke-width="3"/>
            <rect x="16" y="24" width="22" height="16" rx="2" fill="var(--green)"/>
            <path d="M38 29h7l5 6v5H38z" fill="var(--green)"/>
            <circle cx="23" cy="42" r="3.5" fill="var(--green)" stroke="var(--panel)" stroke-width="1.5"/>
            <circle cx="44" cy="42" r="3.5" fill="var(--green)" stroke="var(--panel)" stroke-width="1.5"/>
            <path d="M9 28h5M7 33h7M10 38h4" stroke="var(--green)" stroke-width="2"/>
          </svg>
          <p>Free<br>Shipping</p>
        </div>
      </div>

      <div class="palm-art palm-art-left" role="img" aria-label="Illustration of green palm tree silhouettes"></div>
      <div class="palm-art palm-art-right" role="img" aria-label="Illustration of green palm tree silhouettes"></div>

      <p class="pitch">
        Personal <strong>Protective</strong><br>
        Equipment for<br>
        <strong>Family &amp; Business</strong><br>
        will open <strong>safely</strong>
      </p>

      <address class="contact">
        <div class="contact-icons" aria-hidden="true">
          <svg viewBox="0 0 14 14"><circle cx="7" cy="7" r="6" fill="none" stroke="var(--green)"/><path d="M5 4l1.5 1.5-1 1a5 5 0 002 2l1-1L10 9l-1 1.5C6 10 4 8 3.5 5z" fill="var(--green)"/></svg>
          <svg viewBox="0 0 14 14"><circle cx="7" cy="7" r="6" fill="none" stroke="var(--green)"/><rect x="3.8" y="5" width="6.4" height="4.4" fill="var(--green)"/></svg>
          <svg viewBox="0 0 14 14"><circle cx="7" cy="7" r="6" fill="none" stroke="var(--green)"/><circle cx="7" cy="7" r="3.3" fill="none" stroke="var(--green)"/><path d="M3.7 7h6.6M7 3.7v6.6" stroke="var(--green)" stroke-width=".8"/></svg>
        </div>
        +0 987 654 321<br>
        info@breezeguard.net<br>
        www.breezeguard.net
      </address>
    </section>
  </main>
</body>
</html>
```